Buch-Cover-Design - Lemurion 3.1 - Morgenlied für die Seele der Erdenkinder
Das Design von Glasfalke wurde sehr schnell und professionell erstellt. Ich habe mich außerordentlich gut betreut gefühlt, zumal die Designerin zum einen die Vorgabe excellent umgesetzt und dabei noch eigene Impulse eingebracht hat. Ich bin glücklich und dankbar, sowie hochzufrieden!
Zielgruppe
Ich habe ein Buch geschrieben. Zielgruppe sind Menschen mit dem Genre Spiritualität, Persönlichkeitsentwicklung, Esoterik, Coaching
Aufgabenstellung
Mein Buchtitel lautet: Lemurion 3.1 - Morgenlied für die Seele der Erdenkinder. Es sollte in irgendeiner Form ein spirituelles Cover sein. Gerne darf da auch die 'Lebensblume' als geometrisches Muster in einem Teil des Bildes integriert sein. Die Farben sollten eher hell, weiß, gelb und/oder rosa/lila sein. Keine dunklen Farben. Strahlen wie Sonnenlicht sind auch sehr gut.
Das Buch erscheint in DIN A5 und hat ca. 160 Seiten. Ich freue mich sehr über Ihre Vorschläge! Dankeschön.

```html
<!DOCTYPE html>
<html lang="de">
<head>
<meta charset="utf-8">
<title>Lemurion 3.1 – Buchcover</title>
<link rel="stylesheet" href="https://fonts.googleapis.com/css2?family=Allura&family=Open+Sans:wght@400&display=swap">
<style>
  :root {
    --page-bg: #ece8e4;
    --cover-white: #fbfcfc;
    --ink-deep: #0f5f68;
    --ink-teal: #2a9a9c;
    --ink-mint: #8fe0cf;
    --ink-pale: #d3f3ea;
    --gold: #c9956a;
    --type-teal: #1d6f78;
  }
  html, body {
    margin: 0;
    width: 1200px;
    height: 999px;
    overflow: hidden;
    background: var(--page-bg);
  }
  .book-cover {
    position: absolute;
    left: 280px;
    top: 38px;
    width: 640px;
    height: 922px;
    background: var(--cover-white);
    box-shadow: 0 6px 24px rgba(0,0,0,0.12);
    overflow: hidden;
  }
  .cover-artwork {
    position: absolute;
    inset: 0;
    background:
      radial-gradient(ellipse 55% 30% at 18% 6%, var(--ink-deep) 0%, var(--ink-teal) 45%, rgba(143,224,207,0.5) 75%, transparent 100%),
      radial-gradient(ellipse 45% 22% at 55% 10%, var(--ink-mint) 0%, rgba(211,243,234,0.6) 60%, transparent 100%),
      radial-gradient(ellipse 40% 26% at 22% 80%, var(--ink-mint) 0%, rgba(143,224,207,0.55) 50%, transparent 100%),
      radial-gradient(ellipse 30% 18% at 20% 96%, var(--ink-pale) 0%, transparent 100%),
      radial-gradient(ellipse 30% 40% at 8% 45%, rgba(211,243,234,0.7) 0%, transparent 100%),
      var(--cover-white);
  }
  .cover-title {
    position: absolute;
    left: 150px;
    top: 312px;
    margin: 0;
    font-family: "Allura", cursive;
    font-weight: 400;
    font-size: 78px;
    line-height: 1;
    color: var(--type-teal);
    letter-spacing: 1px;
  }
  .cover-subtitle {
    position: absolute;
    right: 60px;
    top: 420px;
    margin: 0;
    width: 460px;
    font-family: "Open Sans", sans-serif;
    font-size: 25px;
    line-height: 1.35;
    color: var(--type-teal);
    text-align: right;
  }
  .cover-author {
    position: absolute;
    right: 40px;
    bottom: 22px;
    margin: 0;
    font-family: "Allura", cursive;
    font-size: 34px;
    color: var(--type-teal);
  }
</style>
</head>
<body>
  <main class="book-cover">
    <div class="cover-artwork" role="img" aria-label="Türkis-mintfarbene Alkoholtinten-Aquarellflächen mit Goldadern oben links und unten links, überlagert von einem feinen weißen Muster der Blume des Lebens"></div>
    <h1 class="cover-title">Lemurion 3.1</h1>
    <p class="cover-subtitle">Morgenlied für die Seele der Erdenkinder</p>
    <p class="cover-author">Name Autor</p>
  </main>
</body>
</html>
```